Long Established Local Fencing (not swords) Business needs fresh Business Cards

We need fresh double sided business cards for our Fencing Construction business, we are looking for something with our new logo design added, and maybe a photo background ?
We recently had cards made from Cardlyne and we were horrified with what we got back, the quality was terrible, so am looking for high quality format for good printing company to make.
We install Steelmora, Timber paling, Aluminium Slat Screening, Picket (timber and aluminium) and most other fencing installations.
Our website is brankelrails.com.au should you like to learn a bit more.
We do have logo in other formats if required.
We have been in business for over 35 years and we have used this as a "motto" it is on our signage

Industry/Entity Type

Construction

Contact Information for Business Card

Open to ideas, we need 3 x different cards, one generic with no name and 2 x others each with 1 of our bosses name on each, I will put into upload files.

Colors
ec1f27
000000
606060
f5f5f5

Requirements
Must have
• Company Name and Logo
• Address
• Contact details, phone, website, email etc
• Small space to write notes when leaving card at residence
Nice to have
• Our motto "Servicing the Peninsula for over 35 years"

```html
<!DOCTYPE html>
<html lang="en">
<head>
<meta charset="utf-8">
<title>Brankel Rails – Business Cards</title>
<link href="https://fonts.googleapis.com/css2?family=Lato:wght@400;700;900&display=swap" rel="stylesheet">
<style>
  :root {
    --page: #2a2a2b;
    --card: #1c1c1d;
    --card-edge: #262627;
    --silver: #c9c9c9;
    --silver-soft: #a8a8a8;
    --emboss: #6e6e6f;
    --rule: #5a5a5a;
    --note-line: #4a4a4b;
    --brand-red: #ec1f27;
  }
  * { margin: 0; padding: 0; box-sizing: border-box; }
  html, body { width: 1200px; height: 900px; overflow: hidden; }
  body {
    background: var(--page);
    font-family: "Lato", sans-serif;
    position: relative;
  }
  .card {
    position: absolute;
    left: 280px;
    width: 640px;
    height: 366px;
    background: var(--card);
    border: 1px solid var(--card-edge);
    box-shadow: 0 10px 30px rgba(0,0,0,0.45);
  }
  .card-front { top: 68px; }
  .card-back { top: 466px; }

  .brand {
    display: flex;
    align-items: center;
    gap: 14px;
    font-weight: 900;
    letter-spacing: 2px;
    text-transform: uppercase;
  }
  .brand-dot {
    border-radius: 50%;
    flex: none;
    background: var(--brand-red);
  }

  /* Front */
  .front-lockup {
    position: absolute;
    left: 0; right: 0; top: 0; bottom: 0;
    display: flex;
    flex-direction: column;
    align-items: center;
    justify-content: center;
    gap: 18px;
  }
  .card-front .brand {
    color: var(--silver);
    font-size: 44px;
    line-height: 1;
  }
  .card-front .brand-dot { width: 28px; height: 28px; }
  .motto {
    font-size: 14px;
    letter-spacing: 2.5px;
    text-transform: uppercase;
    color: var(--silver-soft);
    padding-top: 14px;
    border-top: 2px solid var(--brand-red);
  }

  /* Back */
  .card-back .brand {
    position: absolute;
    left: 40px;
    top: 66px;
    color: var(--emboss);
    font-size: 30px;
    line-height: 1.1;
  }
  .card-back .brand-dot { width: 22px; height: 22px; }

  .notes {
    position: absolute;
    left: 40px;
    top: 196px;
    width: 236px;
  }
  .notes-label {
    font-size: 12px;
    letter-spacing: 2px;
    text-transform: uppercase;
    color: var(--silver-soft);
  }
  .notes-line {
    height: 28px;
    border-bottom: 1px solid var(--note-line);
  }

  .divider {
    position: absolute;
    left: 316px;
    top: 58px;
    width: 1px;
    height: 250px;
    background: var(--rule);
  }

  .contact {
    position: absolute;
    left: 346px;
    top: 62px;
    color: var(--silver);
  }
  .person-name {
    font-size: 27px;
    font-weight: 400;
    letter-spacing: 1.5px;
    text-transform: uppercase;
  }
  .person-role {
    font-size: 15px;
    color: var(--silver-soft);
    margin-top: 2px;
  }
  .address {
    font-size: 17px;
    line-height: 25px;
    margin-top: 16px;
    color: var(--silver-soft);
  }
  .details { list-style: none; margin-top: 8px; }
  .details li {
    display: flex;
    align-items: center;
    gap: 12px;
    font-size: 17px;
    line-height: 26px;
    color: var(--silver);
  }
  .details svg { width: 12px; height: 12px; flex: none; }
</style>
</head>
<body>

  <section class="card card-front" aria-label="Card front">
    <div class="front-lockup">
      <div class="brand"><span class="brand-dot"></span>Brankel Rails</div>
      <p class="motto">Servicing the Peninsula for over 35 years</p>
    </div>
  </section>

  <section class="card card-back" aria-label="Card back">
    <div class="brand"><span class="brand-dot"></span><span>Brankel<br>Rails</span></div>
    <div class="notes">
      <p class="notes-label">Notes</p>
      <div class="notes-line"></div>
      <div class="notes-line"></div>
      <div class="notes-line"></div>
    </div>
    <div class="divider"></div>
    <div class="contact">
      <p class="person-name">Daniel Hartley</p>
      <p class="person-role">Director</p>
      <p class="address">42 Reedy Lane<br>Kelmora Nsw 2299</p>
      <ul class="details">
        <li>
          <svg viewBox="0 0 12 12" aria-hidden="true"><path d="M2.5 1 L4.5 1 L5.2 3.4 L3.9 4.3 Q5 6.8 7.7 8.1 L8.6 6.8 L11 7.5 L11 9.5 Q11 11 9.5 11 Q1 10.5 1 2.5 Q1 1 2.5 1 Z" fill="#ec1f27"/></svg>
          02 5550 1847
        </li>
        <li>
          <svg viewBox="0 0 12 12" aria-hidden="true"><rect x="1" y="2.5" width="10" height="7" fill="none" stroke="#ec1f27" stroke-width="1.2"/><path d="M1 2.5 L6 6.5 L11 2.5" fill="none" stroke="#ec1f27" stroke-width="1.2"/></svg>
          brankelrails@mailpost.com
        </li>
        <li>
          <svg viewBox="0 0 12 12" aria-hidden="true"><circle cx="6" cy="6" r="5" fill="none" stroke="#ec1f27" stroke-width="1.1"/><ellipse cx="6" cy="6" rx="2.2" ry="5" fill="none" stroke="#ec1f27" stroke-width="1"/><path d="M1 6 H11" stroke="#ec1f27" stroke-width="1"/></svg>
          www.brankelrails.com.au
        </li>
      </ul>
    </div>
  </section>

</body>
</html>
```